Business Card for innovative, tech/consultant company

We are specializing in bringing together Efficiency methodology and Technology for our Business customers. We would like an astonishing business Card that matches this idea.

Target Market(s)

Businesses of medium size or more

Industry/Entity Type

Business Consultant

Contact Information for Business Card

Name, Title, personal email, www, address, phone

Font styles to use
Sans Serif

Colors
3277b5

Requirements
Must have
• - innovative, efficient design
• - good readable
• - Colors must match our logo (blue and grey)
• - the attached font (is licensed by our Company) must be used (Syntax LT)
Should not have
• overloaded

```html
<!DOCTYPE html>
<html lang="en">
<head>
<meta charset="utf-8">
<title>Veralign Business Card</title>
<link rel="stylesheet" href="https://fonts.googleapis.com/css2?family=Open+Sans:wght@400;600&display=swap">
<style>
  :root {
    --brand-blue: #0b84cc;
    --band-blue: #0d87cf;
    --logo-grey: #8e8f91;
    --text-grey: #5b5c5e;
    --rule-grey: #b9bcbf;
    --paper: #ffffff;
    --backdrop: #2b2b2c;
  }
  * { margin: 0; padding: 0; box-sizing: border-box; }
  html, body {
    width: 1200px; height: 750px; overflow: hidden;
    background: var(--backdrop);
    font-family: "Open Sans", Arial, sans-serif;
  }
  .stage { position: relative; width: 1200px; height: 750px; }

  .card {
    position: absolute; top: 226px;
    width: 520px; height: 297px;
    box-shadow: 0 14px 30px rgba(0,0,0,0.45);
  }

  /* Front */
  .card-front { left: 50px; background: var(--brand-blue); color: var(--paper); }
  .card-front .wordmark {
    position: absolute; left: 0; right: 0; top: 96px;
    text-align: center; font-size: 74px; font-weight: 600; letter-spacing: 1px; line-height: 1;
  }
  .card-front .web {
    position: absolute; left: 0; right: 0; top: 212px;
    text-align: center; font-size: 11px; letter-spacing: 4px;
  }

  /* Back */
  .card-back { left: 630px; background: var(--paper); }
  .card-back .band {
    position: absolute; left: 0; right: 0; top: 30px; height: 62px;
    background: var(--band-blue);
    border-top: 3px solid var(--rule-grey);
    border-bottom: 3px solid var(--rule-grey);
    color: var(--paper);
    padding: 10px 0 0 46px;
  }
  .card-back .name { font-size: 17px; font-weight: 600; line-height: 1.15; }
  .card-back .title { font-size: 12px; line-height: 1.3; }
  .card-back .address {
    position: absolute; left: 88px; top: 128px;
    font-size: 11.5px; line-height: 1.5; color: var(--text-grey);
  }
  .card-back .contacts {
    position: absolute; left: 70px; top: 184px; list-style: none;
    font-size: 11.5px; line-height: 1.55; color: var(--text-grey);
  }
  .card-back .contacts li { display: flex; align-items: center; gap: 8px; }
  .card-back .contacts svg { width: 12px; height: 12px; flex: none; fill: var(--brand-blue); }
  .card-back .wordmark {
    position: absolute; right: 40px; top: 140px;
    font-size: 50px; font-weight: 600; line-height: 1; color: var(--logo-grey);
  }
</style>
</head>
<body>
<main class="stage">
  <section class="card card-front" aria-label="Card front">
    <div class="wordmark">Veralign</div>
    <div class="web">www.veralign.com</div>
  </section>

  <section class="card card-back" aria-label="Card back">
    <div class="band">
      <div class="name">Mara Lindqvist</div>
      <div class="title">President</div>
    </div>
    <address class="address" style="font-style:normal">
      412 Harbor Lane<br>Clearfield, NY 10990
    </address>
    <ul class="contacts">
      <li>
        <svg viewBox="0 0 24 24" aria-hidden="true"><path d="M6.6 10.8a15 15 0 0 0 6.6 6.6l2.2-2.2a1 1 0 0 1 1-.25 11.4 11.4 0 0 0 3.6.57 1 1 0 0 1 1 1V20a1 1 0 0 1-1 1A17 17 0 0 1 3 4a1 1 0 0 1 1-1h3.5a1 1 0 0 1 1 1c0 1.25.2 2.45.57 3.6a1 1 0 0 1-.25 1z"/></svg>
        555 0143 2207
      </li>
      <li>
        <svg viewBox="0 0 24 24" aria-hidden="true"><path d="M2 5h20v14H2z M2 5l10 8 10-8" fill="none" stroke="#0b84cc" stroke-width="2.5"/></svg>
        mara@veralign.com
      </li>
      <li>
        <svg viewBox="0 0 24 24" aria-hidden="true"><circle cx="12" cy="12" r="10"/><path d="M2 12h20M12 2c3 3 3 17 0 20M12 2c-3 3-3 17 0 20" fill="none" stroke="#fff" stroke-width="1.5"/></svg>
        www.veralign.com
      </li>
    </ul>
    <div class="wordmark">Veralign</div>
  </section>
</main>
</body>
</html>
```